Company profile infograph to describe key facts about a company

We need to design an infograph.
The Idea of the infograph is to describe a company in one sheet. Company name, company address, financials, recent changes and other data related to the company.
I have attached a brief. The first slide is what the design currently looks, the 3 second slides are how it should look. Please be creative and take ideas from other infographs! The main idea is that when a person sees the infograph, the first impression is that she understands what's up with the company.
Industry/Entity Type
It Company
Number of Pages Required
1 page
Font styles to use
Other font styles liked:
- Avenir Next
Look and feel
Each slider illustrates characteristics of the customer's brand and the style your logo design should communicate.

```html
<!DOCTYPE html>
<html lang="en">
<head>
<meta charset="utf-8">
<title>Norvek – Company Profile</title>
<link href="https://fonts.googleapis.com/css2?family=Nunito+Sans:wght@400;600;700;800;900&display=swap" rel="stylesheet">
<style>
  :root{
    --stage:#55546e;
    --sheet:#ffffff;
    --panel:#efefef;
    --blue:#0b55a3;
    --blue-dark:#0a3f82;
    --bar:#3a9ad9;
    --green:#8cc63f;
    --orange:#c8461f;
    --sky:#2ba6dd;
    --logo-gray:#a3a3a3;
    --ink:#1c1c1c;
    --muted:#555;
  }
  *{box-sizing:border-box;margin:0;padding:0}
  html,body{width:1200px;height:1000px;overflow:hidden}
  body{background:var(--stage);font-family:"Nunito Sans",sans-serif;color:var(--ink);position:relative}

  .sheet{position:absolute;left:45px;top:35px;width:1110px;height:930px;background:var(--sheet);padding:12px}
  .panel{position:relative;width:100%;height:100%;background:var(--panel);border-radius:14px}

  .brand{position:absolute;top:18px;left:0;right:0;display:flex;justify-content:center;align-items:center;gap:22px}
  .brand-dot{width:70px;height:70px;border-radius:50%;background:var(--green)}
  .brand-name{font-size:104px;font-weight:600;color:var(--logo-gray);line-height:1;letter-spacing:-1px}
  .address{position:absolute;top:138px;left:0;right:0;text-align:center;font-size:16px;font-weight:800}

  .highlights{position:absolute;left:30px;right:30px;top:172px;height:132px;background:var(--blue);border-radius:14px;display:flex;align-items:center;justify-content:space-around;padding:0 20px;color:#fff}
  .highlight{display:flex;align-items:center;gap:12px}
  .highlight svg{flex:none}
  .hl-big{font-size:40px;font-weight:900;line-height:.95;letter-spacing:-.5px}
  .hl-small{font-size:17px;font-weight:800;line-height:1.05}
  .hl-spaced{font-size:17px;font-weight:800;letter-spacing:6px;text-align:center}
  .hl-row{display:flex;align-items:flex-end;gap:4px}

  .box{position:absolute;border-radius:16px;border:6px solid}
  .finance{left:30px;top:322px;width:498px;height:560px;border-color:var(--green)}
  .changes{left:548px;top:322px;width:508px;height:240px;border-color:var(--orange)}
  .tech{left:548px;top:580px;width:508px;height:302px;border-color:var(--sky)}

  .box-title{display:flex;align-items:center;justify-content:center;gap:12px;margin-top:22px;color:var(--blue)}
  .box-title .big{font-size:46px;font-weight:900;line-height:.9}
  .box-title .sub{font-size:17px;font-weight:800;line-height:1}

  .chart-label{margin:28px 0 0 34px;font-size:14px;color:var(--muted)}
  .chart{display:block;margin:4px auto 0}

  .fin-table{width:440px;margin:0 auto;font-size:13px;font-weight:600;text-align:center}
  .fin-row{display:grid;grid-template-columns:repeat(5,1fr);height:24px;align-items:center;border-radius:12px}
  .fin-row.head{background:var(--blue-dark);color:#fff;font-weight:800;font-size:14px}
  .fin-row.alt{background:#fff}

  .change-list{list-style:none;padding:18px 26px}
  .change{display:flex;align-items:center;gap:14px;margin-bottom:10px}
  .change-title{font-size:25px;font-weight:900;color:var(--blue);line-height:1}
  .change-note{font-size:16px;font-weight:800;color:var(--blue);line-height:1.2}

  .tech-title{display:flex;align-items:center;gap:12px;margin:22px 0 0 46px;color:var(--green);font-size:27px;font-weight:900}
  .tech-grid{display:flex;justify-content:space-around;align-items:flex-end;padding:14px 18px 0}
  .tech-item{text-align:center;color:var(--sky);display:flex;flex-direction:column;align-items:center}
  .tech-cat{font-size:18px;font-weight:800;line-height:1;margin-bottom:10px}
  .tech-marks{display:flex;gap:6px}
  .tech-mark{width:44px;height:44px;background:var(--green);border-radius:4px}
  .tech-name{font-size:11px;font-weight:700;margin-top:8px}
</style>
</head>
<body>
<div class="sheet">
  <div class="panel">
    <header class="brand">
      <span class="brand-dot"></span>
      <span class="brand-name">norvek</span>
    </header>
    <p class="address">Harbor Street 42 10245 NY, USA</p>

    <section class="highlights">
      <div class="highlight">
        <svg width="56" height="56" viewBox="0 0 56 56" fill="none" stroke="var(--green)" stroke-width="5">
          <circle cx="28" cy="28" r="19"/><circle cx="28" cy="28" r="8"/>
          <path d="M28 2v12M28 42v12M2 28h12M42 28h12"/>
        </svg>
        <div><div class="hl-big">FOCUSES</div><div class="hl-small">ON DIGITAL BUSINESS</div></div>
      </div>
      <div class="highlight">
        <svg width="52" height="44" viewBox="0 0 52 44" fill="none" stroke="var(--green)" stroke-width="6">
          <path d="M2 10h12c10 0 14 24 24 24h6M2 34h12c10 0 14-24 24-24h6"/>
          <path d="M40 2l9 8-9 8M40 26l9 8-9 8" stroke-width="5"/>
        </svg>
        <div>
          <div class="hl-small" style="font-size:21px">LOT OF</div>
          <div class="hl-big">CHANGES</div>
          <div class="hl-spaced">RECENTLY</div>
        </div>
      </div>
      <div class="highlight">
        <svg width="50" height="50" viewBox="0 0 50 50" fill="none" stroke="var(--green)" stroke-width="6">
          <rect x="4" y="8" width="36" height="36" rx="4"/>
          <path d="M12 24l9 9 24-28"/>
        </svg>
        <div>
          <div class="hl-small">PERFORMS</div>
          <div class="hl-row"><span class="hl-big">LOWER</span><span class="hl-small">THAN<br>AVERAGE</span></div>
          <div class="hl-spaced" style="letter-spacing:4px">IN INDUSTRY</div>
        </div>
      </div>
    </section>

    <section class="box finance">
      <div class="box-title">
        <svg width="60" height="46" viewBox="0 0 60 46">
          <rect x="2" y="10" width="52" height="32" rx="3" fill="var(--blue)"/>
          <rect x="9" y="16" width="38" height="20" rx="2" fill="#fff"/>
          <circle cx="28" cy="26" r="7" fill="var(--blue)"/>
          <rect x="8" y="2" width="50" height="6" rx="2" fill="var(--blue)"/>
        </svg>
        <div><div class="big">BASIC</div><div class="sub">FINANCIAL INFO</div></div>
      </div>
      <p class="chart-label">Liikevaihdon kehitys</p>
      <svg class="chart" width="440" height="190" viewBox="0 0 440 190" font-family="Nunito Sans, sans-serif" font-size="10" font-weight="700">
        <g stroke="#bbb" stroke-dasharray="2 3">
          <line x1="0" y1="18" x2="390" y2="18"/><line x1="0" y1="60" x2="390" y2="60"/>
          <line x1="0" y1="102" x2="390" y2="102"/><line x1="0" y1="144" x2="390" y2="144"/>
        </g>
        <g fill="#444"><text x="396" y="14">750</text><text x="396" y="56">350</text><text x="396" y="98">100</text><text x="396" y="140">50</text></g>
        <g fill="var(--blue-dark)">
          <rect x="4" y="180" width="6" height="8"/><rect x="17" y="178" width="6" height="10"/><rect x="30" y="176" width="6" height="12"/>
        </g>
        <g fill="var(--bar)">
          <rect x="43" y="172" width="6" height="16"/><rect x="56" y="166" width="6" height="22"/><rect x="69" y="160" width="6" height="28"/>
          <rect x="82" y="164" width="6" height="24"/><rect x="95" y="166" width="6" height="22"/><rect x="108" y="162" width="6" height="26"/>
          <rect x="121" y="156" width="6" height="32"/><rect x="134" y="146" width="6" height="42"/><rect x="147" y="134" width="6" height="54"/>
          <rect x="160" y="122" width="6" height="66"/><rect x="173" y="108" width="6" height="80"/><rect x="186" y="94" width="6" height="94"/>
          <rect x="199" y="82" width="6" height="106"/><rect x="212" y="94" width="6" height="94"/><rect x="225" y="106" width="6" height="82"/>
          <rect x="238" y="118" width="6" height="70"/><rect x="251" y="104" width="6" height="84"/><rect x="264" y="118" width="6" height="70"/>
          <rect x="277" y="128" width="6" height="60"/><rect x="290" y="140" width="6" height="48"/><rect x="303" y="150" width="6" height="38"/>
          <rect x="316" y="160" width="6" height="28"/><rect x="329" y="168" width="6" height="20"/><rect x="342" y="176" width="6" height="12"/>
        </g>
        <g fill="var(--green)">
          <rect x="147" y="124" width="6" height="8"/><rect x="173" y="98" width="6" height="8"/>
          <rect x="251" y="94" width="6" height="8"/><rect x="264" y="106" width="6" height="8"/><rect x="277" y="118" width="6" height="8"/>
        </g>
      </svg>
      <div class="fin-table">
        <div class="fin-row head"><span>2010 / 09</span><span>2011 / 09</span><span>2012 / 12</span><span>2013 / 12</span><span>2014 / 12</span></div>
        <div class="fin-row"><span>6457</span><span>5480</span><span>7469</span><span>5077</span><span>5768</span></div>
        <div class="fin-row alt"><span>103.10</span><span>-15.10</span><span>9.00</span><span>-15.00</span><span>13.60</span></div>
        <div class="fin-row"><span>109</span><span>10</span><span>-94</span><span>56</span><span>70</span></div>
        <div class="fin-row alt"><span>1.90</span><span>1.20</span><span>-1.40</span><span>2.30</span><span>6.60</span></div>
        <div class="fin-row"><span>70</span><span>69</span><span>69</span><span>64</span><span>61</span></div>
      </div>
    </section>

    <section class="box changes">
      <ul class="change-list">
        <li class="change">
          <svg width="40" height="40" viewBox="0 0 40 40" fill="var(--orange)">
            <circle cx="11" cy="8" r="6"/><path d="M2 22c0-6 4-8 9-8s9 2 9 8z"/>
            <circle cx="29" cy="22" r="6"/><path d="M20 38c0-6 4-8 9-8s9 2 9 8z"/>
          </svg>
          <div><div class="change-title">CHANGES IN MANAGEMENT</div><div class="change-note">Anna and new worker</div></div>
        </li>
        <li class="change">
          <svg width="40" height="40" viewBox="0 0 40 40" fill="var(--orange)">
            <circle cx="20" cy="6" r="5"/><path d="M13 17c0-5 3-6 7-6s7 1 7 6z"/>
            <path d="M19 17h2v5h12v6h-2v-4H9v4H7v-6h12z"/>
            <circle cx="8" cy="31" r="4"/><path d="M2 40c0-4 3-5 6-5s6 1 6 5z"/>
            <circle cx="32" cy="31" r="4"/><path d="M26 40c0-4 3-5 6-5s6 1 6 5z"/>
          </svg>
          <div><div class="change-title">ORGANIZATIONAL CHANGES</div><div class="change-note">New structure in company</div></div>
        </li>
        <li class="change">
          <svg width="40" height="40" viewBox="0 0 40 40" fill="var(--orange)">
            <path d="M14 4h10l-3 5h-4z"/><circle cx="19" cy="18" r="9"/>
            <path d="M2 30h8l8 3h10l8-5 2 3-10 8H10l-8-2z"/>
          </svg>
          <div><div class="change-title">INVESTMENTS M&amp;A</div><div class="change-note">Company buys it's competitor</div></div>
        </li>
      </ul>
    </section>

    <section class="box tech">
      <h2 class="tech-title">
        <svg width="52" height="40" viewBox="0 0 52 40" fill="var(--green)">
          <rect x="8" y="12" width="30" height="20" rx="2"/><rect x="2" y="33" width="42" height="5" rx="2"/>
          <rect x="30" y="2" width="6" height="6"/><rect x="38" y="2" width="6" height="6"/><rect x="46" y="6" width="5" height="5"/><rect x="40" y="12" width="5" height="5"/>
        </svg>
        USED TECHNOLOGIES
      </h2>
      <div class="tech-grid">
        <div class="tech-item"><div class="tech-cat">Marketing</div><div class="tech-marks"><span class="tech-mark"></span></div><div class="tech-name">Adreach remarketing</div></div>
        <div class="tech-item"><div class="tech-cat">e-Comerce</div><div class="tech-marks"><span class="tech-mark"></span></div><div class="tech-name">Shoplane</div></div>
        <div class="tech-item"><div class="tech-cat">Web<br>page</div><div class="tech-marks"><span class="tech-mark"></span></div><div class="tech-name">Pagecraft</div></div>
        <div class="tech-item"><div class="tech-cat">Social<br>Media</div><div class="tech-marks"><span class="tech-mark"></span><span class="tech-mark"></span></div><div class="tech-name">Friendline / Chirper</div></div>
      </div>
    </section>
  </div>
</div>
</body>
</html>
```